we can communicate on this, but i want to follow the approach we took on Pell|Quorn & Tillet but i feel the card front needs the black background and the platinum and gold logo. The back? I am open. we can use the same info from PQ&T. Vellum Crest is an enhanced equity investment fund - basically a very exclusive boutique hedge fund that uses only stock options. very advanced things. hope you are interested

Contact Information for Business Card

Dr. Owen T. Brisket, CFA
Scientifique de fusée financière
555.014.2296
TheDoc4793@mailvessel.example

4718 Fennel Brook Way N.
West Fargo, ND 58078

No web site

Colors

Designer to choose colors to be used in the design.

Requirements
Nice to have
• I tend to prefer the most visible applications of the logo to include logo and name, the logo version with a black background and the gold and platinum components separated by the black. I see this working well for a single side (logo and name - this is card front to me).
• I am fairly open to other treatments on the reverse side with the data. To me, it makes sense to have a different color rendition of the logo on the reverse and it may be a muted black tone on tone or an oversized portion that would have spot UV. Or, the reverse may play with colors and layout
Should not have
• Other colors = no no
• Decorative font

```html
<!DOCTYPE html>
<html lang="en">
<head>
<meta charset="utf-8">
<title>Vellum Crest – Business Cards</title>
<link href="https://fonts.googleapis.com/css2?family=Open+Sans:wght@400;600;700&display=swap" rel="stylesheet">
<style>
  :root {
    --backdrop: #d4d5d4;
    --card-black: #0d0d0d;
    --tone-dark: #1c1c1c;
    --tone-mid: #262626;
    --gold: #c9a227;
    --white: #f4f4f4;
    --muted: #9a9a9a;
  }
  * { margin: 0; padding: 0; box-sizing: border-box; }
  html, body {
    width: 1200px; height: 900px; overflow: hidden;
    background: var(--backdrop);
    font-family: "Open Sans", Arial, sans-serif;
  }
  .sheet {
    position: relative; width: 1200px; height: 900px;
    display: flex; align-items: center; justify-content: center; gap: 80px;
  }
  .card {
    width: 400px; height: 400px;
    background: var(--card-black);
    box-shadow: 0 6px 18px rgba(0,0,0,0.25);
    display: flex; flex-direction: column; align-items: center; justify-content: center;
    text-align: center;
  }

  /* Tone-on-tone side */
  .card--tonal .brand-mark {
    width: 140px; height: 140px; border-radius: 50%;
    background: linear-gradient(160deg, var(--tone-mid), #141414);
    margin-bottom: 26px;
  }
  .card--tonal .brand-name {
    font-weight: 700; font-size: 36px; letter-spacing: 2px;
    color: var(--tone-dark); text-transform: uppercase; white-space: nowrap;
  }

  /* Information side */
  .card--info .brand-lockup {
    display: flex; flex-direction: column; align-items: center; gap: 10px; margin-bottom: 20px;
  }
  .card--info .brand-dot {
    width: 56px; height: 56px; border-radius: 50%; background: var(--gold);
  }
  .card--info .brand-name {
    font-weight: 700; font-size: 24px; letter-spacing: 1.5px;
    color: var(--white); text-transform: uppercase; white-space: nowrap;
  }
  .holder-name {
    color: var(--gold); font-weight: 700; font-size: 17px; white-space: nowrap;
  }
  .holder-name .credential { font-size: 12px; }
  .holder-title {
    color: var(--muted); font-size: 12px; margin-top: 2px;
  }
  .divider {
    width: 36px; height: 2px; background: var(--muted); margin: 14px auto;
  }
  .address { color: var(--muted); font-size: 12px; line-height: 1.5; }
  .contact-list {
    list-style: none; margin-top: 10px;
    color: var(--muted); font-size: 12px; line-height: 1.7;
  }
  .contact-list li { display: flex; align-items: center; justify-content: center; gap: 6px; white-space: nowrap; }
  .contact-list svg { width: 11px; height: 11px; fill: none; stroke: var(--gold); stroke-width: 2; }
</style>
</head>
<body>
  <main class="sheet">
    <section class="card card--tonal" aria-label="Card front, tone-on-tone">
      <div class="brand-mark"></div>
      <div class="brand-name">Vellum Crest</div>
    </section>

    <section class="card card--info" aria-label="Card back, contact details">
      <div class="brand-lockup">
        <div class="brand-dot"></div>
        <div class="brand-name">Vellum Crest</div>
      </div>
      <p class="holder-name">Dr. Owen T. Brisket, <span class="credential">CFA</span></p>
      <p class="holder-title">Scientifique des Fusées Financières</p>
      <div class="divider"></div>
      <p class="address">4718 Fennel Brook Way N.<br>West Fargo, ND 58078</p>
      <ul class="contact-list">
        <li>
          <svg viewBox="0 0 12 12"><rect x="3" y="1" width="6" height="10" rx="1"/></svg>
          555.014.2296
        </li>
        <li>
          <svg viewBox="0 0 12 12"><rect x="1" y="2.5" width="10" height="7"/><path d="M1 2.5 L6 7 L11 2.5"/></svg>
          TheDoc4793@mailvessel.example
        </li>
      </ul>
    </section>
  </main>
</body>
</html>
```